Collagen Tub Packaging Design for a New Brand

PLEASE DON'T SEND ANY NEW DESIGNS WE JUST HAVE TO DECIDE WITH MY PARTNERS THANKS A LOT.
I've created a very detailed document & design examples of what we like in certain designs and what we don't.

There are 3 documents:
1- Brief for the Design (please read it before designing)
2- Brand Design Examples that we like (and why we like them)
3- Die cut for the packaging design. This will be it's dimensions.

We are NOT looking for someone to micro-manage. In contrast, we want someone to help us express our ideas better with their design. Nothing I say in these briefs are there to limit the creativity of the designer, because if we knew exactly what we wanted we would do it ourselves but we trust the designer's expertise in this packaging design.

In short: We want our brand to feel premium, high-quality & trust worthy with it's design not feeling very busy or bloated. We don't have a logo source file, but you'll get the idea of what we want when you see it).

Let me know if you have any further questions, will answer each question real fast.

Thanks.

Target Market(s)

Pretty much everyone above 25+ in Turkey because nearly all of them are using are collagens so our audience is wild.

Industry/Entity Type

Collagen - Health, Wellness & Supplements

Font styles to use
Serif
Sans Serif

Colors

Designer to choose colors to be used in the design.

Requirements
Must have
• Our design should be distinct, a design style which everyone can identify from 10 meters away if they know the product. This is a MUST have for us. It's up to designer to achieve it. This can be just a simple color palette aswell.
Should not have
• It shouldn't feel bloated and very busy. Please avoid very detailed icons (as a rule of thumb, if you can make it work great)

```html
<!DOCTYPE html>
<html lang="en">
<head>
<meta charset="utf-8">
<title>Solvana Hydrolyzed Collagen Peptides – Tub Label</title>
<link href="https://fonts.googleapis.com/css2?family=Oswald:wght@400;500;600&family=Literata:wght@500;600&display=swap" rel="stylesheet">
<style>
  :root{
    --paper:#f7f8f8;
    --band-grey:#9a9c98;
    --brand-grey:#9b9d9a;
    --ink:#2f3133;
    --blue-light:#4a9bd0;
    --blue-deep:#0058a3;
    --scene-light:#eceeee;
    --scene-mid:#d3d5d5;
    --icon-grey:#8e9091;
  }
  *{margin:0;padding:0;box-sizing:border-box}
  html,body{width:1200px;height:1200px;overflow:hidden;background:#ffffff}
  .label{position:relative;width:1200px;height:1200px;background:var(--paper);font-family:"Oswald",sans-serif;color:var(--ink)}
  .top-band{position:absolute;left:60px;right:60px;top:130px;height:26px;background:linear-gradient(90deg,#a9aba7,#8d8f8b 50%,#a9aba7)}
  .brand{position:absolute;left:0;width:900px;top:205px;text-align:center;font-family:"Literata",serif;font-weight:500;font-size:78px;letter-spacing:4px;color:var(--brand-grey)}
  .qualifier{position:absolute;left:178px;top:355px;font-weight:600;font-size:36px;letter-spacing:4px;color:var(--ink)}
  .product-name{position:absolute;left:168px;top:388px;font-weight:500;font-size:200px;line-height:1;letter-spacing:2px;
    background:linear-gradient(90deg,var(--blue-light),var(--blue-deep) 65%,#2b83c6);-webkit-background-clip:text;background-clip:text;color:transparent}
  .scene{position:absolute;left:150px;top:605px;width:700px;height:300px;border-radius:40px 40px 0 0;
    background:radial-gradient(ellipse at 50% 80%,var(--scene-mid),var(--scene-light) 60%,var(--paper) 100%)}
  .subtitle{position:absolute;left:633px;top:610px;font-weight:500;font-size:44px;letter-spacing:3px;color:#1f74bb}
  .claims{position:absolute;left:628px;top:688px;list-style:none;font-weight:500;font-size:30px;line-height:54px;color:var(--ink)}
  .claims li::before{content:"• "}
  .type-banner{position:absolute;left:228px;top:918px;width:490px;height:76px;display:flex;align-items:center;justify-content:center;
    background:linear-gradient(90deg,var(--blue-light),#1f6fb4);font-family:"Literata",serif;font-weight:500;font-size:42px;color:#ffffff}
  .net-weight{position:absolute;left:0;width:900px;top:1020px;text-align:center;font-weight:500;font-size:32px;letter-spacing:4px;color:var(--ink)}
  .features{position:absolute;left:930px;top:220px;width:210px;list-style:none;text-align:center;color:var(--ink)}
  .feature{height:210px;display:flex;flex-direction:column;align-items:center}
  .feature svg,.feature .icon-slot{width:70px;height:80px;margin-bottom:22px}
  .icon-slot{display:block;background:linear-gradient(180deg,#e2e3e3,#cfd1d1);border-radius:10px}
  .feature-title{font-size:19px;font-weight:400;line-height:1.3}
  .feature-sub{font-size:17px;font-weight:400;letter-spacing:.5px;line-height:1.4}
  .feature svg{fill:none;stroke:var(--icon-grey);stroke-width:2.5;stroke-linejoin:round}
</style>
</head>
<body>
<main class="label">
  <div class="top-band"></div>
  <div class="brand">Solvana</div>

  <div class="qualifier">HIDROLYZED</div>
  <h1 class="product-name">COLLAGEN</h1>

  <div class="scene" role="img" aria-label="Soft grey engraved illustration of cows grazing in a pasture with trees and rolling hills"></div>

  <div class="subtitle">PEPTIDES</div>
  <ul class="claims">
    <li>HIGH ABSORPTION</li>
    <li>HIGH-QUALITY</li>
    <li>UNFLAVOURED</li>
  </ul>

  <div class="type-banner">Collagen Type I, II &amp; III</div>
  <div class="net-weight">620g · DIETARY FOOD SUPPLEMENT</div>

  <ul class="features">
    <li class="feature">
      <svg viewBox="0 0 70 80" aria-hidden="true">
        <path d="M35 18 L40 38 L56 44 L40 50 L35 70 L30 50 L14 44 L30 38 Z"/>
        <path d="M14 6 L16 13 L22 15 L16 17 L14 24 L12 17 L6 15 L12 13 Z"/>
        <path d="M58 60 L60 66 L65 68 L60 70 L58 76 L56 70 L51 68 L56 66 Z"/>
      </svg>
      <span class="feature-title">Benefits</span>
      <span class="feature-sub">HAIR, SKIN &amp; NAILS</span>
    </li>
    <li class="feature">
      <svg viewBox="0 0 70 80" aria-hidden="true">
        <path d="M10 44 H50 V66 Q50 74 42 74 H18 Q10 74 10 66 Z"/>
        <path d="M50 50 H68"/>
        <path d="M14 44 Q22 26 34 34 Q42 28 48 44"/>
        <path d="M30 8 L32 14 L38 16 L32 18 L30 24 L28 18 L22 16 L28 14 Z"/>
      </svg>
      <span class="feature-title">Easy to Mix</span>
      <span class="feature-sub">POWDER COLLAGEN</span>
    </li>
    <li class="feature">
      <span class="icon-slot" role="img" aria-label="Small line icon of a cow's head"></span>
      <span class="feature-title">100% Grass Fed</span>
      <span class="feature-sub">BOVINE COLLAGEN</span>
    </li>
    <li class="feature">
      <svg viewBox="0 0 70 80" aria-hidden="true">
        <path d="M36 10 L54 18 L54 36 L36 44 L18 36 L18 18 Z"/>
        <path d="M18 18 L36 26 L54 18 M36 26 V44"/>
        <path d="M12 44 L28 50 L28 68 L12 74 Z"/>
        <path d="M28 50 L44 44 V62 L28 68"/>
      </svg>
      <span class="feature-title">Sugar FREE</span>
    </li>
  </ul>
</main>
</body>
</html>
```